Tarnby Group letterhead

Hi,

I need a letterhead template created for our business. This should be done in word format and A4 size. The images need to not move in the template ie when I am adding writing in etc. and should flow on when I get to a second page.

I have attached our logo templates below.

Other details to include on the letterhead somewhere are:

0438 915 267
Max@Tarnbyelectrical.example.au
PO Box 817 Marrowvale NSW 2190
ABN: 57 318 962 407

Thanks!

```html
<!DOCTYPE html>
<html lang="en">
<head>
<meta charset="utf-8">
<title>Tarnby Group Letterhead</title>
<link href="https://fonts.googleapis.com/css2?family=Lato:wght@400;700;900&family=Open+Sans:wght@400;600&family=Tangerine:wght@700&display=swap" rel="stylesheet">
<style>
  :root {
    --backdrop: #a0a0a0;
    --paper: #ffffff;
    --ink: #3a3a3a;
    --ink-dark: #1a1a1a;
    --accent: #ee5322;
    --faint: #dcdadb;
  }
  * { box-sizing: border-box; margin: 0; padding: 0; }
  html, body { width: 1077px; height: 1200px; overflow: hidden; }
  body { background: var(--backdrop); position: relative; font-family: "Lato", sans-serif; color: var(--ink); }
  .sheet {
    position: absolute; left: 156px; top: 79px; width: 766px; height: 1080px;
    background: var(--paper); overflow: hidden;
  }
  .brand {
    position: absolute; left: 52px; top: 40px; display: flex; align-items: center; gap: 10px;
  }
  .brand-dot { width: 30px; height: 30px; border: 5px solid var(--ink-dark); border-radius: 50%; }
  .brand-name { font-family: "Lato", sans-serif; font-weight: 900; font-size: 21px; letter-spacing: 1px; color: var(--accent); text-transform: uppercase; }
  .contact {
    position: absolute; left: 517px; top: 60px; padding-left: 11px;
    border-left: 1px solid var(--accent);
    font-family: "Open Sans", sans-serif; font-size: 13px; line-height: 17px; color: var(--ink-dark);
  }
  .contact .address { margin-bottom: 5px; }
  .contact-row { display: flex; align-items: center; gap: 6px; }
  .contact-row svg { width: 10px; height: 10px; fill: var(--accent); flex: none; }
  .watermark { position: absolute; left: 244px; top: 390px; width: 280px; height: 280px; }
  .letter { position: absolute; left: 52px; top: 253px; width: 664px; font-size: 14.5px; line-height: 17px; }
  .date { color: var(--accent); font-size: 15.5px; margin-bottom: 20px; }
  .recipient { margin-bottom: 15px; line-height: 18px; font-size: 14.8px; }
  .salutation { color: var(--accent); font-weight: 700; font-size: 18.5px; margin: 10px 0 16px; }
  .body p { text-align: justify; margin-bottom: 17px; }
  .closing { margin-top: 36px; font-size: 14.8px; }
  .signature { font-family: "Tangerine", cursive; font-weight: 700; font-size: 46px; color: var(--accent); margin-top: 18px; margin-left: 4px; }
  .footer { position: absolute; left: 0; bottom: 0; width: 766px; height: 36px; }
  .footer-band { position: absolute; left: 0; bottom: 0; width: 100%; height: 15px; background: var(--accent); }
  .footer-rule { position: absolute; top: 12px; height: 2.5px; background: var(--ink-dark); }
  .footer-rule.left { left: 0; width: 244px; }
  .footer-rule.right { left: 519px; right: 0; }
  .footer-rule::after { content: ""; position: absolute; top: -1.5px; width: 5px; height: 5px; border-radius: 50%; background: var(--ink-dark); }
  .footer-rule.left::after { right: -2px; }
  .footer-rule.right::after { left: -2px; }
  .abn-tab {
    position: absolute; left: 267px; top: 1px; width: 232px; height: 35px;
    background: var(--accent); border-radius: 12px 12px 0 0;
    color: #fff; font-family: "Open Sans", sans-serif; font-weight: 600; font-size: 15px;
    display: flex; align-items: center; justify-content: center; padding-bottom: 4px;
  }
</style>
</head>
<body>
  <main class="sheet">
    <header>
      <div class="brand">
        <span class="brand-dot"></span>
        <span class="brand-name">Tarnby Group</span>
      </div>
      <address class="contact" style="font-style:normal">
        <div class="address">PO Box 817 Marrowvale NSW 2190</div>
        <div class="contact-row">
          <svg viewBox="0 0 10 10"><path d="M1 3c0-1 1-2 4-2s4 1 4 2v1H7V3H3v1H1zM2 5h6l1 4H1z"/></svg>
          <span>+ 0438 915 267</span>
        </div>
        <div class="contact-row">
          <svg viewBox="0 0 10 10"><path d="M0 2h10v1L5 6 0 3zM0 4l5 3 5-3v4H0z"/></svg>
          <span>Max@Tarnbyelectrical.example.au</span>
        </div>
        <div class="contact-row">
          <svg viewBox="0 0 10 10"><circle cx="5" cy="5" r="4.5"/></svg>
          <span>www.tarnbyelectrical.example.au</span>
        </div>
      </address>
    </header>

    <svg class="watermark" viewBox="0 0 280 280" aria-hidden="true">
      <circle cx="140" cy="140" r="128" fill="none" stroke="var(--faint)" stroke-width="20" opacity="0.9"/>
    </svg>

    <section class="letter">
      <p class="date">Dec-19-2024</p>
      <p class="recipient">Mr, Peter Lane<br>President</p>
      <p class="recipient">Crestline Corporation<br>123 Street Name, Suite# 10<br>City, State, 120023</p>
      <h1 class="salutation">Dear Mr, Peter</h1>
      <div class="body">
        <p>Lorem ipsum dolor sit amet, consectetur adipisicing elit, sed do eiusmod tempor incididunt ut labore et dolore magna aliqua. Ut enim ad minim veniam, quis nostrud exercitation ullamco laboris nisi ut aliquip ex ea commodo consequat. Duis aute irure dolor in reprehenderit in voluptate velit esse cillum dolore eu fugiat nulla pariatur.</p>
        <p>Lorem ipsum dolor sit amet, consectetur adipisicing elit, sed do eiusmod tempor incididunt ut labore et dolore magna aliqua. Ut enim ad minim veniam, quis nostrud exercitation ullamco laboris nisi ut aliquip ex ea commodo consequat. Duis aute irure dolor in reprehenderit in voluptate velit esse cillum dolore eu fugiat nulla pariatur.</p>
        <p>Lorem ipsum dolor sit amet, consectetur adipisicing elit, sed do eiusmod tempor incididunt ut labore et dolore magna aliqua. Ut enim ad minim veniam, quis nostrud exercitation ullamco laboris nisi ut aliquip ex ea commodo consequat.</p>
        <p>Excepteur sint occaecat cupidatat non proident, sunt in culpa qui officia deserunt mollit anim id est laborum. re et dolore magnam aliquam quaerat voluptatem.</p>
      </div>
      <p class="closing">Regards</p>
      <p class="signature">Liam Hartley</p>
    </section>

    <footer class="footer">
      <div class="footer-band"></div>
      <div class="footer-rule left"></div>
      <div class="footer-rule right"></div>
      <div class="abn-tab">ABN: 57 318 962 407</div>
    </footer>
  </main>
</body>
</html>
```